UK Online Escort Directory Requires a Redesigned Email Marketing Campaign (4 emails total)

These emails should be designed as marketing emails that will be sent out to approx 10,000 potential customers on a by monthly basis. The designs should be innovative, professional designs that are capable of capturing a readers attention in the blink of an eye.

We have posted this job as our in-house design capabilities are not able to create professional email designs, we therefore require a designer to redesign our email marketing campaign (4 emails total) to a professional level.

The content of the emails will be provided, along with the 5 emails that we are currently sending and the company logo. This should give the potential designer all that they need to redesign the campaign to a professional level.

Please see attached brief for more information on what is required from each individual email.

Target Market(s)

Escorts throughout the UK

Industry/Entity Type

Escort

Font styles to use
Serif
Sans Serif

Requirements
Must have
• Instant recognition of what's being offered.
Nice to have
• Imaginative / inspirational designs.
Should not have
• Any unnecessary wording or text.

```html
<!DOCTYPE html>
<html lang="en">
<head>
<meta charset="utf-8">
<title>Velvet Listings UK – Email Campaign</title>
<link rel="stylesheet" href="https://fonts.googleapis.com/css2?family=Open+Sans:ital,wght@0,400;0,600;0,700;1,400;1,600;1,700&display=swap">
<style>
  :root{
    --page:#d8c3d5;
    --panel:#ffffff;
    --plum:#9b3f8f;
    --ink:#333333;
    --muted:#6b6b6b;
    --line:#dcdcdc;
    --soft:#f3f3f3;
    --cream:#fff8cf;
    --cream-edge:#ecdf95;
    --gold:#e3a21a;
    --link:#2f62c9;
    --photo-a:#e7c9a4;
    --photo-b:#b98c6a;
    --photo-c:#c8b7cf;
  }
  *{box-sizing:border-box;margin:0;padding:0}
  html,body{width:1200px;height:2620px;overflow:hidden}
  body{background:var(--page);font-family:"Open Sans",Arial,sans-serif;color:var(--ink);position:relative}

  .email{position:absolute;left:152px;width:896px;background:var(--panel);border-top:6px solid var(--plum);padding:22px 40px 0;text-align:center}
  .email--one{top:60px;height:528px}
  .email--two{top:680px;height:480px}
  .email--three{top:1272px;height:488px}
  .email--four{top:1860px;height:740px}

  .social{display:flex;justify-content:center;gap:10px}
  .social span{width:26px;height:26px;border-radius:50%;background:#1a1a1a;display:block}

  .brand{margin-top:14px;font-weight:600;font-size:40px;line-height:1.1;color:var(--plum);letter-spacing:.5px}

  .lead{font-size:15px;color:var(--muted);margin:22px 0 14px}

  .listing{display:flex;background:var(--cream);border:2px solid var(--cream-edge);text-align:left;position:relative}
  .listing__photo{flex:none;background:linear-gradient(160deg,var(--photo-a),var(--photo-b))}
  .listing__body{padding:14px 18px;flex:1}
  .listing__badge{position:absolute;top:8px;right:14px;font-size:12px;font-weight:700;color:var(--plum)}
  .listing__badge b{color:var(--gold);letter-spacing:1px}
  .listing__name{font-weight:700;font-size:26px}
  .listing__place{font-size:13px;color:var(--muted);font-weight:400;margin-left:8px}
  .listing__text{font-size:14px;line-height:1.45;margin-top:8px}

  .listing--large{margin:0 40px}
  .listing--large .listing__photo{width:140px;height:150px}
  .listing--large .listing__body{padding-top:34px}

  .actions{display:flex;justify-content:center;gap:18px;margin-top:26px}
  .btn{background:var(--plum);color:#fff;font-weight:700;font-size:15px;padding:12px 20px;border-radius:4px}

  .footnote{position:absolute;left:0;right:0;top:604px;text-align:center;font-size:16px;color:#3c3c3c}
  .footnote a{color:var(--link)}

  .notice{background:var(--soft);border:1px solid var(--line);padding:18px 20px;font-size:16px;margin:34px 60px 0;text-align:left}
  .notice a{color:var(--link);font-weight:700}
  .facts{display:flex;gap:22px;margin:22px 60px 0}
  .facts div{flex:1;background:var(--soft);border:1px solid var(--line);padding:16px 18px;font-size:15px;line-height:1.5;text-align:left;color:#555}

  .offers{display:flex;gap:30px;margin-top:30px}
  .offer{flex:1;min-width:0}
  .offer__title{font-style:italic;font-weight:700;font-size:14px;margin-bottom:8px}
  .offer .listing__photo{width:80px;height:96px}
  .offer .listing__body{padding:8px 10px}
  .offer .listing__badge{font-size:10px;top:6px;right:8px}
  .offer .listing__name{font-size:15px;margin-top:14px}
  .offer .listing__place{font-size:10px;margin-left:5px}
  .offer .listing__text{font-size:11px;line-height:1.4;margin-top:4px}

  .signoff{text-align:left;margin:30px 0 0 130px;font-size:15px;line-height:1.9}
  .signoff a{color:var(--link);font-weight:700;font-style:italic}

  .free{margin:30px 150px 0;border:1px solid var(--line);padding:14px 16px}
  .free__title{font-size:26px;color:#555;letter-spacing:1px}
  .free__sub{font-size:13px;font-style:italic;color:#777;margin-top:12px;border-top:1px solid var(--line);padding-top:10px}
  .special{font-size:16px;color:#555;margin:20px 0 18px}
  .profile{display:flex;margin:0 100px;background:var(--cream);border:2px solid var(--cream-edge);text-align:left;height:170px;overflow:hidden}
  .profile__photo{flex:none;width:130px;height:140px;margin:13px;background:linear-gradient(160deg,var(--photo-c),var(--photo-b))}
  .profile__body{flex:1;padding:16px 10px}
  .profile__name{font-size:22px;font-weight:700}
  .profile__text{font-size:13px;color:#555;line-height:1.45;margin-top:8px}
  .profile__more{font-size:12px;color:var(--plum);font-weight:600;margin-top:8px}
  .profile__side{flex:none;width:130px;background:var(--plum);color:#fff;font-weight:700;font-size:15px;display:flex;align-items:center;justify-content:center;border-top-left-radius:70px 85px;border-bottom-left-radius:70px 85px}
  .email--four .signoff{margin-top:24px}
</style>
</head>
<body>

<section class="email email--one">
  <div class="social"><span></span><span></span><span></span><span></span></div>
  <div class="brand">Velvet Listings UK</div>
  <p class="lead">Last week this ad was viewed 963 times and produced 135 phone calls for just £49.49pm.</p>
  <div class="listing listing--large">
    <div class="listing__photo" role="img" aria-label="Advertiser profile photo"></div>
    <div class="listing__badge">RECOMMENDED <b>★★★★★</b></div>
    <div class="listing__body">
      <div class="listing__name">Marisa, 22 <span class="listing__place">Birmingham City Centre Escort</span></div>
      <p class="listing__text">New to Birmingham - Hallow Guys, my name is Marisa, I am from Sweden. My pictures are 100% Genuine, I am a glamour model. Call me Kisses Marisa xxx xxx I am a deep throat expert x OWO+CIM</p>
    </div>
  </div>
  <div class="actions"><span class="btn">Take a look</span><span class="btn">Post an ad</span></div>
</section>
<p class="footnote">For anything any problems you can view this <a>link</a></p>

<section class="email email--two">
  <div class="social"><span></span><span></span><span></span><span></span></div>
  <div class="brand">Velvet Listings UK</div>
  <p class="notice">Be seen on <a>www.velvetlistings.co.uk</a></p>
  <div class="facts">
    <div>Your ad will be seen by 15,000 customers a day</div>
    <div>See where we are on search engines Type [your town + escorts] e.g.Birmingham escorts</div>
  </div>
  <div class="actions"><span class="btn">Take a look</span><span class="btn">Post an ad</span></div>
</section>

<section class="email email--three">
  <div class="social"><span></span><span></span><span></span><span></span></div>
  <div class="brand">Velvet Listings UK</div>
  <div class="offers">
    <div class="offer">
      <p class="offer__title">This premium ad on Homepage for 30 days is £XX.XX</p>
      <div class="listing">
        <div class="listing__photo" role="img" aria-label="Advertiser profile photo"></div>
        <div class="listing__badge">RECOMMENDED <b>★★★★★</b></div>
        <div class="listing__body">
          <div class="listing__name">Marisa, 22 <span class="listing__place">Birmingham City Centre</span></div>
          <p class="listing__text">New to Birmingham. Friendly, genuine photos, available daily for outcalls and incalls. Call me today.</p>
        </div>
      </div>
    </div>
    <div class="offer">
      <p class="offer__title">This premium ad on SERPS for 30 days is £49.49</p>
      <div class="listing">
        <div class="listing__photo" role="img" aria-label="Advertiser profile photo"></div>
        <div class="listing__badge">RECOMMENDED <b>★★★★★</b></div>
        <div class="listing__body">
          <div class="listing__name">Marisa, 22 <span class="listing__place">Birmingham City Centre</span></div>
          <p class="listing__text">New to Birmingham. Friendly, genuine photos, available daily for outcalls and incalls. Call me today.</p>
        </div>
      </div>
    </div>
  </div>
  <div class="signoff">
    Check us out : <a>www.velvetlistings.co.uk</a><br>
    Contact us : <a>support@velvetlistings.co.uk for more information</a><br>
    <b>The VLUK Team.</b>
  </div>
</section>

<section class="email email--four">
  <div class="social"><span></span><span></span><span></span><span></span></div>
  <div class="brand">Velvet Listings UK</div>
  <div class="free">
    <div class="free__title">ONE MONTH FREE EMAIL</div>
    <p class="free__sub">In this email we will be offering potential customers their first month free</p>
  </div>
  <p class="special">Special Offer - First month free on VLUK - No Credit Card Needed - No Obligation</p>
  <div class="profile">
    <div class="profile__photo" role="img" aria-label="Advertiser profile photo"></div>
    <div class="profile__body">
      <div class="profile__name">Dr Orla Penfield</div>
      <p class="profile__text">Lorem ipsum dolor sit amet, consectetur adipiscing elit, sed do eiusr.</p>
      <p class="profile__more">Read More</p>
    </div>
    <div class="profile__side">Add Sections</div>
  </div>
  <div class="signoff">
    Be seen by 15,000 people a day – Have a look<br>
    Check us out : <a>www.velvetlistings.co.uk</a><br>
    Contact us : <a>support@velvetlistings.co.uk for more information</a><br>
    The VLUK Team.
  </div>
</section>

</body>
</html>
```